Presentation Template for Copperleaf Studio

We would like to have a template for our presentations since we have a new logo and want a new general image.

The new template should have as minimum Cover/Title Page, Bullets page and Regular page. We have a new logo and need the template to mach with it. For the bullets and regular page we want the design no take much part for including content, so we would like something that makes the slides look good but leaving most of room free for writing.

We would like the logo on the footer of the regular slides (not of course for the cover, dividers etc)

I'm attaching de logo here. Our logo colours are #b80016, #006ac6 and black

Thank you

Industry/Entity Type

It Company

Font styles to use
Other font styles liked:
• Maven Pro

Colors
ec1f27
0355a3
000000

Requirements
Must have
• Presentation template with Cover/Title Page, Bullets page and Regular page. Must match with our new logo.
• We would like the logo on the footer of the regular slides (not of course for the cover, dividers etc)
• Our logo colours are #b80016, #006ac6 and black
Nice to have
• Other type of slides, special bullets etc
Should not have
• I don't know

```html
<!DOCTYPE html>
<html lang="en">
<head>
<meta charset="utf-8">
<title>Copperleaf Studio – Presentation Template</title>
<link href="https://fonts.googleapis.com/css2?family=Maven+Pro:wght@400;500;700&family=Roboto:ital,wght@0,400;0,700;1,400&display=swap" rel="stylesheet">
<style>
:root{
  --red:#e0161f;
  --red-deep:#b80016;
  --blue:#0a5fbf;
  --blue-deep:#0355a3;
  --ink:#111;
  --grey:#555;
  --paper:#fff;
  --teal:#3fb5a6;
}
*{box-sizing:border-box;margin:0;padding:0}
html,body{width:1200px;height:3197px;overflow:hidden;background:#fff}
body{font-family:"Roboto",Arial,sans-serif;color:var(--ink)}
.deck{display:grid;grid-template-columns:581px 581px;column-gap:38px;row-gap:31px;padding:3px 0 0}
.slide{position:relative;width:581px;height:327px;overflow:hidden;background:var(--paper);box-shadow:0 0 0 1px #e4e4e4}
.abs{position:absolute}
h2.title{font-family:"Maven Pro",Arial,sans-serif;font-weight:700;font-size:21px}
.on-blue{color:#fff}
p.body{font-size:8.4px;line-height:1.4;color:var(--grey)}
.on-blue p.body{color:#fff}
.corner-tl{position:absolute;left:0;top:0}
.page-no{position:absolute;right:0;bottom:0;width:46px;height:46px}
.page-no span{position:absolute;right:6px;bottom:5px;color:#fff;font-size:11px;font-weight:700}
.foot-logo{position:absolute;right:14px;bottom:8px;display:flex;align-items:center;gap:3px;font-family:"Maven Pro",sans-serif;font-weight:700;font-size:6.5px;color:var(--red)}
.foot-logo i{display:block;width:7px;height:7px;background:var(--red)}
.slide.numbered .foot-logo{right:52px}
.brand{display:flex;align-items:center;gap:10px;font-family:"Maven Pro",sans-serif;font-weight:700;color:var(--red)}
.brand i{display:block;background:var(--red)}
.bullets{display:flex;flex-direction:column;gap:10px}
.bullets .item{display:flex;gap:12px}
.bullets .star{width:12px;height:12px;flex:none;margin-top:1px}
.bullets h3{font-size:10.5px;font-weight:700;font-family:"Maven Pro",sans-serif;color:var(--blue-deep)}
.bullets p{font-size:8.4px;line-height:1.35;color:#333}
.bullets.light{color:#fff}
.bullets.light h3,.bullets.light p{color:#fff}
.photo{position:absolute}
.band-blue{position:absolute;background:var(--blue)}
.quote-i{font-style:italic;color:#444;font-size:10px;line-height:1.4}
.cols p{font-size:7.4px;line-height:1.45;color:#444;margin-bottom:7px}
.cols strong{color:#111}
.callout{background:var(--red-deep);color:#fff;padding:8px 10px;font-size:7.4px;line-height:1.4;margin-bottom:7px}
</style>
</head>
<body>
<svg width="0" height="0" style="position:absolute">
  <defs>
    <symbol id="star" viewBox="0 0 24 24"><path d="M12 1l3.2 7.3 7.8.7-5.9 5.2 1.8 7.8L12 18l-6.9 4 1.8-7.8L1 9l7.8-.7z" fill="currentColor"/></symbol>
    <symbol id="corner" viewBox="0 0 90 90"><polygon points="0,0 60,0 0,60" fill="#0a5fbf"/><polygon points="0,42 42,0 58,0 0,58" fill="#e0161f"/></symbol>
    <symbol id="pageno" viewBox="0 0 46 46"><polygon points="46,0 46,46 0,46" fill="#b80016"/></symbol>
  </defs>
</svg>

<main class="deck">

<!-- 1 Cover -->
<section class="slide cover">
  <svg class="abs" style="left:0;top:0" width="210" height="327" viewBox="0 0 210 327">
    <polygon points="0,0 150,0 0,150" fill="#0a5fbf"/>
    <polygon points="0,0 175,0 20,160" fill="#0a5fbf" opacity=".55"/>
    <polygon points="0,110 110,0 128,0 0,128" fill="#e0161f"/>
    <polygon points="0,180 60,240 0,300" fill="#0a5fbf" opacity=".25"/>
  </svg>
  <svg class="abs" style="right:0;bottom:0" width="90" height="70" viewBox="0 0 90 70">
    <polygon points="90,0 90,70 20,70" fill="#0a5fbf"/><polygon points="90,30 90,70 50,70" fill="#e0161f"/>
  </svg>
  <div class="abs" style="left:212px;top:58px;width:260px">
    <h1 style="font-family:'Maven Pro',sans-serif;font-weight:500;font-size:22px;color:var(--red);line-height:1.2">Lorem ipsum dolor<br>sit amet</h1>
    <p style="color:var(--blue);font-size:11.5px;line-height:1.35;margin-top:8px">Veri audire sententiae cu vel. Ius deserunt invenire id, eam ullum persius denique an.</p>
  </div>
  <div class="brand abs" style="left:212px;top:212px;font-size:24px"><i style="width:26px;height:26px"></i>Copperleaf Studio</div>
</section>

<!-- 2 About Us -->
<section class="slide on-blue" style="background:var(--blue)">
  <svg class="abs" style="left:0;top:0" width="160" height="327" viewBox="0 0 160 327">
    <polygon points="0,0 110,0 0,110" fill="#fff"/><polygon points="0,80 80,0 96,0 0,96" fill="#e0161f"/>
  </svg>
  <svg class="abs" style="right:0;bottom:0" width="70" height="70" viewBox="0 0 70 70"><polygon points="70,0 70,70 0,70" fill="#fff"/><polygon points="70,30 70,70 30,70" fill="#e0161f"/></svg>
  <h2 class="title abs" style="left:290px;top:20px;width:260px;text-align:center">About Us</h2>
  <div class="abs" style="left:300px;top:60px;width:245px;text-align:center">
    <p class="body" style="margin-bottom:8px">Lorem ipsum dolor sit amet, eas inani prodesset ne. Vel audire sententiae cu vel. Ius deserunt invenire id, eam ullum persius denique an. Iudico facilisi epicuri ea eos. Tempor bonorum minimum ea mea, vis ad autem mucius.</p>
    <p class="body">Per postea menandri te. Vocibus menandrum mei no, sit iudico graeco ea. Pri ne accusam liberavisse, vero sanctus usu id. Quem diam pertinacia his ne, in nihil eusmod consetuum eum. Duo omnesque noluisse repudiandae ei.</p>
  </div>
</section>

<!-- 3 Collaborative Innovation -->
<section class="slide numbered">
  <div class="band-blue" style="left:0;top:0;width:581px;height:270px"></div>
  <svg class="abs" style="left:0;top:0" width="50" height="50" viewBox="0 0 50 50"><polygon points="0,0 38,0 0,38" fill="#fff"/><polygon points="0,26 26,0 34,0 0,34" fill="#e0161f"/></svg>
  <h2 class="title abs on-blue" style="left:50px;top:22px">Collaborative Innovation</h2>
  <div class="bullets light abs" style="left:50px;top:75px;width:470px">
    <div class="item"><svg class="star"><use href="#star"/></svg><div><h3>Harbor Supply Team</h3><p>We had another strong day in the Retail business on Wednesday with 46 loads. The market moved up sharp late in the morning. In addition to the large market move, our team was able to close a low-risk contract with partner teams causing some supply disruption at times. Three members jumped in to secure carriers and source product to support the orders we were bringing in. It was a total team effort to get these loads delivered.</p></div></div>
    <div class="item"><svg class="star"><use href="#star"/></svg><div><h3>The Billing Team</h3><p>Over the last week this team of professionals pulled together to get January billing closed successfully and February invoicing on track for all business units. This required discretionary effort and focus from the entire team!</p></div></div>
  </div>
  <div class="foot-logo"><i></i>Copperleaf Studio</div>
  <div class="page-no"><svg width="46" height="46"><use href="#pageno"/></svg><span>3</span></div>
</section>

<!-- 4 Family Business -->
<section class="slide numbered">
  <div class="band-blue" style="left:0;top:0;width:581px;height:270px"></div>
  <svg class="abs" style="left:0;top:0" width="50" height="50" viewBox="0 0 50 50"><polygon points="0,0 38,0 0,38" fill="#fff"/><polygon points="0,26 26,0 34,0 0,34" fill="#e0161f"/></svg>
  <h2 class="title abs on-blue" style="left:50px;top:22px">Family Business</h2>
  <div class="abs on-blue" style="left:40px;top:70px;width:380px">
    <p class="body" style="margin-bottom:8px">Lorem ipsum dolor sit amet, no tempor menandrum intellegam vim, qui ei graeco denique. Primis sonet ad mei, qui ut vero menandri salutandi. Ius viverra posidonium regulone id, ut ne eirmod volutpat interpretaris. Mundi repudiare coitidieque qui te.</p>
    <p class="body">Dicta volumus denique nec eu, te nam dispitantis disputationi. Quo case definiebas quaerendum et. Ius simul melore probissed eu. Cum eu dolore legere, cu nisl ceteri facilisis aliquando, duo at habeo consectetuer. Usu ea vide augue adversarium, audiam utroque sensibus in duo, minimum gubergren et per. Autem modus usu eu. Alterum phaedrum volutpat no mei.</p>
  </div>
  <div class="photo" role="img" aria-label="Close-up photograph of a camera lens" style="left:446px;top:70px;width:104px;height:104px;background:radial-gradient(circle,#d9d9d9 0%,#6d6d6d 30%,#1c1c1c 60%,#050505 100%)"></div>
  <div class="foot-logo"><i></i>Copperleaf Studio</div>
  <div class="page-no"><svg width="46" height="46"><use href="#pageno"/></svg><span>4</span></div>
</section>

<!-- 5 Branded text slide -->
<section class="slide numbered">
  <svg class="corner-tl" width="60" height="60"><use href="#corner"/></svg>
  <div class="brand abs" style="left:195px;top:40px;font-size:20px"><i style="width:20px;height:20px"></i>Copperleaf Studio</div>
  <div class="abs" style="left:70px;top:140px;width:440px;text-align:center">
    <p class="body" style="margin-bottom:8px;color:#333">We met Ridge Equipment at the regional conference several weeks ago. On Wed., we got a call from the team at 4:30pm; they needed fuel for a portable heater system at the Eastbank Plant. Our team jumped into action and was on site with a first fuel delivery within 30 minutes. This is a direct take away from a key competitor and a testament to both our business development and operations team for follow-up and execution.</p>
    <p class="body" style="color:#333">Texas Retail delivered to a new site in Granger, TX. This new site has an anticipated volume of 250,000. Our Fuel Team successfully secured Mesa Drilling as a new West Texas crew assignment that launched service on Wednesday. We are bidding on work with a partner for the North Dakota region in our Frac division and if successful will launch our first one in late February.</p>
  </div>
  <div class="foot-logo"><i></i>Copperleaf Studio</div>
  <div class="page-no"><svg width="46" height="46"><use href="#pageno"/></svg><span>5</span></div>
</section>

<!-- 6 Branded text slide -->
<section class="slide numbered">
  <svg class="corner-tl" width="60" height="60"><use href="#corner"/></svg>
  <div class="brand abs" style="left:195px;top:40px;font-size:20px"><i style="width:20px;height:20px"></i>Copperleaf Studio</div>
  <div class="abs" style="left:70px;top:140px;width:440px;text-align:center">
    <p class="body" style="margin-bottom:8px;color:#333"><strong>The EPS team</strong> was able to close several opportunities this week. New contracts were signed with several regional firms. They also added 4 new generator accounts with northern partners, Northwind Labs and Orchard Systems. Lastly the team was able to secure a fuel polishing opportunity with a local firm. Nice work, Dana and Priya!</p>
    <p class="body" style="color:#333">Not to be outdone, the Commercial Team was able to land some noteworthy opportunities this week as well. Marco Vell was able to get a contract signed with a steel mill. This is a 15,000 gpm account that will be using a FleetTrack Management System. Way to bring this one home Marco!</p>
  </div>
  <div class="foot-logo"><i></i>Copperleaf Studio</div>
  <div class="page-no"><svg width="46" height="46"><use href="#pageno"/></svg><span>6</span></div>
</section>

<!-- 7 Tallgrass Capital -->
<section class="slide numbered">
  <svg class="corner-tl" width="60" height="60"><use href="#corner"/></svg>
  <h2 class="title abs" style="left:50px;top:40px">Tallgrass Capital</h2>
  <div class="bullets abs" style="left:50px;top:95px;width:470px;color:var(--blue-deep)">
    <div class="item"><svg class="star"><use href="#star"/></svg><div><h3>Harbor Supply Team</h3><p>We had another strong day in the Retail business on Wednesday with 46 loads. The market moved up sharp late in the morning. In addition to the large market move, our team was able to close a low-risk contract with partner teams causing some supply disruption at times. Three members jumped in to secure carriers and source product to support the orders we were bringing in. It was a total team effort to get these loads delivered.</p></div></div>
    <div class="item"><svg class="star"><use href="#star"/></svg><div><h3>The Billing Team</h3><p>Over the last week this team of professionals pulled together to get January billing closed successfully and February invoicing on track for all business units. This required discretionary effort and focus from the entire team!</p></div></div>
  </div>
  <div class="foot-logo"><i></i>Copperleaf Studio</div>
  <div class="page-no"><svg width="46" height="46"><use href="#pageno"/></svg><span>7</span></div>
</section>

<!-- 8 Family Business band -->
<section class="slide numbered">
  <h2 class="title abs" style="left:0;top:20px;width:581px;text-align:center;font-size:18px">Family Business</h2>
  <div class="band-blue" style="left:0;top:75px;width:581px;height:120px"></div>
  <div class="photo" role="img" aria-label="Photograph of stacked shipping containers under a cloudy sky" style="left:0;top:60px;width:260px;height:150px;background:linear-gradient(180deg,#9fc4e8 0%,#e9eef3 45%,#b33a2e 70%,#3c5f8d 100%);clip-path:polygon(0 0,100% 0,82% 100%,0 100%)"></div>
  <div class="abs on-blue" style="left:300px;top:100px;width:240px">
    <p class="body">Dicta volumus denique nec eu, te nam dispitantis disputationi. Quo case definiebas quaerendum et. Ius simul melore probissed eu. Cum eu dolore legere, cu nisl ceteri facilisis aliquando, duo at habeo consectetuer. Usu ea vide augue adversarium, audiam utroque sensibus in duo, minimum gubergren et per. Autem modus usu eu. Alterum phaedrum volutpat no mei.</p>
  </div>
  <div class="foot-logo"><i></i>Copperleaf Studio</div>
  <div class="page-no"><svg width="46" height="46"><use href="#pageno"/></svg><span>8</span></div>
</section>

<!-- 9 Collaborative Innovation white -->
<section class="slide numbered">
  <svg class="corner-tl" width="60" height="60"><use href="#corner"/></svg>
  <h2 class="title abs" style="left:50px;top:40px">Collaborative Innovation</h2>
  <div class="bullets abs" style="left:50px;top:95px;width:470px;color:var(--blue-deep)">
    <div class="item"><svg class="star"><use href="#star"/></svg><div><h3>Harbor Supply Team</h3><p>We had another strong day in the Retail business on Wednesday with 46 loads. The market moved up sharp late in the morning. In addition to the large market move, our team was able to close a low-risk contract with partner teams causing some supply disruption at times. Three members jumped in to secure carriers and source product to support the orders we were bringing in. It was a total team effort to get these loads delivered.</p></div></div>
    <div class="item"><svg class="star"><use href="#star"/></svg><div><h3>The Billing Team</h3><p>Over the last week this team of professionals pulled together to get January billing closed successfully and February invoicing on track for all business units. This required discretionary effort and focus from the entire team!</p></div></div>
  </div>
  <div class="foot-logo"><i></i>Copperleaf Studio</div>
  <div class="page-no"><svg width="46" height="46"><use href="#pageno"/></svg><span>9</span></div>
</section>

<!-- 10 Collaborative Innovation photo -->
<section class="slide numbered">
  <div class="band-blue" style="left:0;top:0;width:581px;height:270px"></div>
  <div class="photo" role="img" aria-label="Photograph of a modern glass office building" style="left:260px;top:40px;width:321px;height:230px;background:linear-gradient(135deg,#e6ecf2 0%,#9aa6b2 45%,#4b5560 100%);clip-path:polygon(100% 0,100% 100%,0 100%)"></div>
  <h2 class="title abs on-blue" style="left:30px;top:22px">Collaborative Innovation</h2>
  <div class="abs on-blue" style="left:30px;top:65px;width:270px">
    <p class="body" style="margin-bottom:8px">Lorem ipsum dolor sit amet, cum purto docendi eleifend ex, ut sapientem philosophia an. Per iudico docendi pertinax id. Timeam verear interesset mei ei, ponderum omnittam eum et. His at amet adhuc reque. Animal timeam tempam per id, nonumy utamur aliquandam in sed. Autem dolor definitiones qua at, ad homero quidam verear vel.</p>
    <p class="body">Per iudico docendi pertinax id. Timeam verear interesset mei ei, ponderum omnittam eum et. His at amet adhuc reque. Animal timeam tempam per id, nonumy aliquandam in sed. Autem dolor definitiones qua at, ad homero quidam verear vel.</p>
  </div>
  <div class="foot-logo"><i></i>Copperleaf Studio</div>
  <div class="page-no"><svg width="46" height="46"><use href="#pageno"/></svg><span>10</span></div>
</section>

<!-- 11 Employee Satisfaction -->
<section class="slide numbered">
  <h2 class="abs" style="left:30px;top:95px;font-family:'Maven Pro',sans-serif;font-weight:400;font-size:24px;color:var(--red);line-height:1.2">Employee<br>Satisfaction</h2>
  <div class="abs" style="left:30px;top:175px;width:220px">
    <p class="quote-i">"This is a great site! Much better than our previous platform."</p>
    <p class="quote-i" style="margin-top:12px">"Loving these new options for creating an event!" #userfriendlyherewecome</p>
  </div>
  <div class="photo" role="img" aria-label="Smartphone showing a banking app feed for Northgate Bank" style="left:300px;top:10px;width:200px;height:280px;border-radius:22px;background:linear-gradient(180deg,#e9ecef 0%,#f7f7f7 15%,#2f63b0 15%,#2f63b0 30%,#fafafa 30%,#fafafa 100%);box-shadow:0 0 0 6px #dfe2e6"></div>
  <div class="foot-logo"><i></i>Copperleaf Studio</div>
  <div class="page-no"><svg width="46" height="46"><use href="#pageno"/></svg><span>11</span></div>
</section>

<!-- 12 Main Competence -->
<section class="slide numbered">
  <div class="photo" role="img" aria-label="Faded photograph of pencils in a cup on a desk" style="left:0;top:0;width:581px;height:327px;background:linear-gradient(90deg,#fbfbfb 0%,#f1f1f1 55%,#d9d9d9 75%,#f4f4f4 100%)"></div>
  <svg class="corner-tl" width="60" height="60"><use href="#corner"/></svg>
  <h2 class="abs" style="left:40px;top:100px;font-family:'Maven Pro',sans-serif;font-weight:400;font-size:28px;color:var(--blue);line-height:1.2">Main<br>Competence</h2>
  <p class="abs" style="left:40px;top:185px;width:250px;font-size:10.5px;line-height:1.35;color:var(--red)">Customer database development or management of customer database trough dedicated digital services</p>
  <div class="foot-logo"><i></i>Copperleaf Studio</div>
  <div class="page-no"><svg width="46" height="46"><use href="#pageno"/></svg><span>12</span></div>
</section>

<!-- 13 Three Columns -->
<section class="slide numbered">
  <h2 class="title abs" style="left:20px;top:12px;font-size:18px">Three Columns</h2>
  <div class="cols abs" style="left:20px;top:42px;width:540px;display:grid;grid-template-columns:1fr 1fr 1fr;gap:18px">
    <div>
      <p><strong>Lorem ipsum dolor sit amet, sea dicit suavitate consulatu in.</strong></p>
      <p>Propriae incorrupte per in. Eam ad debitis epicuri, vix ea posim noluisse argumentum, id graecis percipit assueverit sit. Munere graecis an eum.</p>
      <p>Per ea fugit dissentiet. Ea nobis consul patrioque sed. Facer menandri sapientem eam ut, te sed aeque inermis temporibus. Nam te case fastidii, in maluisset sadipscing sed, et eam decore integre maiestatis.</p>
    </div>
    <div>
      <p>Cum eu vidit mutat aeterno, no ius harum habemus euripidis, et his tota nonumy graeco. Eum nemore deserunt pertinax et. Fugit consul iuctius mel cu.</p>
      <div class="callout">In cetero audiam delicata eos, usu ut paulo eloquentiam ullamcorper.</div>
      <p>Quo in pertinax electram patrioque. Id debet civilian vix, quo et munere ut. No dicit epicure periculis mea. Ubique dicening repetitiones vix ad, operam pericula omittantur per ne. No modus latine iudicabit est.</p>
    </div>
    <div>
      <p>Electram liberavisse consectetuer te eam, nam lorem inermis periculis eu, no sit dicunt feugait molestiae. Vix case erat eu, vix impedit dissentiet et, eu lorem congue molestie mei. Cu cum maluisset constituto. Sint nostrud accusata id duo. His at suscipit operiam eloquentiam.</p>
      <p>Tractatos argumentum suscipiantur eam te. Cu vivendum insolens consequat mea. Dicta dicit usu eu, soleat eloquentiam eu pri.</p>
    </div>
  </div>
  <div class="foot-logo"><i></i>Copperleaf Studio</div>
  <div class="page-no"><svg width="46" height="46"><use href="#pageno"/></svg><span>13</span></div>
</section>

<!-- 14 Two Columns -->
<section class="slide numbered">
  <h2 class="title abs" style="left:20px;top:12px;font-size:18px">Two Columns</h2>
  <div class="cols abs" style="left:20px;top:42px;width:540px;display:grid;grid-template-columns:1fr 1fr;gap:22px">
    <div>
      <div class="callout" style="font-size:8px">Lorem ipsum dolor sit amet, sea dicit suavitate consulatu in. Propriae incorrupte per in. Eam ad debitis epicuri, vix ea posim noluisse argumentum.</div>
      <p>Per ea fugit dissentiet. Ea nobis consul patrioque sed. Facer menandri sapientem eam ut, te sed aeque inermis temporibus. Nam te case fastidii, in maluisset sadipscing sed, et eam decore integre maiestatis. Mei at mollis repudiare, vitae verear torquatos ex vix.</p>
      <p>Cum eu vidit mutat aeterno, no ius harum habemus euripidis, et his tota nonumy graeco. Eum nemore deserunt pertinax et. Fugit consul iuctius mel cu. In cetero audiam delicata eos, usu ut paulo eloquentiam ullamcorper, nostrud molestie cotidieque ex usu.</p>
    </div>
    <div>
      <p>Lorem ipsum dolor sit amet, sea dicit suavitate consulatu in. Propriae incorrupte per in. Eam ad debitis epicuri, vix ea posim noluisse argumentum, id graecis percipit assueverit sit. Munere graecis an eum.</p>
      <p>"Per ea fugit dissentiet. Ea nobis consul patrioque sed. Facer menandri sapientem eam ut, te sed aeque inermis temporibus. Nam te case fastidii, in maluisset sadipscing sed, et eam decore integre maiestatis. Mei at mollis repudiare, vitae verear torquatos ex vix."</p>
      <p>Cum eu vidit mutat aeterno, no ius harum habemus euripidis, et his tota nonumy graeco. Eum nemore deserunt pertinax et. Fugit consul iuctius mel cu. In cetero audiam delicata eos, usu ut paulo eloquentiam ullamcorper, nostrud molestie cotidieque ex usu.</p>
    </div>
  </div>
  <div class="foot-logo"><i></i>Copperleaf Studio</div>
  <div class="page-no"><svg width="46" height="46"><use href="#pageno"/></svg><span>14</span></div>
</section>

<!-- 15 Map -->
<section class="slide numbered">
  <h2 class="title abs" style="left:20px;top:12px;font-size:18px">Map Title</h2>
  <div class="photo" role="img" aria-label="World map with highlighted regions in red and orange" style="left:40px;top:55px;width:490px;height:235px;background:linear-gradient(90deg,#c8102e 0%,#c8102e 30%,#f5a623 45%,#f5a623 100%);opacity:.85;border-radius:40px 90px 60px 120px"></div>
  <div class="foot-logo"><i></i>Copperleaf Studio</div>
  <div class="page-no"><svg width="46" height="46"><use href="#pageno"/></svg><span>15</span></div>
</section>

<!-- 16 Quote -->
<section class="slide numbered">
  <div class="photo" role="img" aria-label="Blue-tinted photograph of an office interior" style="left:0;top:0;width:581px;height:327px;background:linear-gradient(135deg,#1d6fcb 0%,#0a5fbf 55%,#084d9c 100%)"></div>
  <h2 class="abs" style="left:20px;top:20px;font-family:'Maven Pro',sans-serif;font-weight:400;font-size:28px;color:#fff">Quote</h2>
  <div class="abs" style="left:40px;top:120px;font-size:64px;line-height:1;color:#fff;font-family:Georgia,serif">“</div>
  <p class="abs" style="left:95px;top:140px;width:400px;color:#fff;font-size:15px;line-height:1.35">Lorem ipsum dolor sit amet, denique phaedrum ex ius. Per eu populo albucius invidunt, accumsan vivendum pro no. Volumus corpora omnesque cu mel.</p>
  <div class="abs" style="left:490px;top:200px;font-size:64px;line-height:1;color:#fff;font-family:Georgia,serif">”</div>
  <div class="foot-logo" style="color:#fff"><i style="background:#fff"></i>Copperleaf Studio</div>
  <div class="page-no"><svg width="46" height="46"><use href="#pageno"/></svg><span>16</span></div>
</section>

<!-- 17 Process chart -->
<section class="slide numbered">
  <h2 class="title abs" style="left:20px;top:12px;font-size:18px;color:#16324f">Chart Title Here</h2>
  <svg class="abs" style="left:15px;top:60px" width="550" height="230" viewBox="0 0 550 230">
    <defs><linearGradient id="wave" x1="0" x2="1"><stop offset="0" stop-color="#2f9f8f"/><stop offset="1" stop-color="#7fcf8a"/></linearGradient></defs>
    <path d="M15 115 H50 C80 115 80 75 110 75 C140 75 140 155 170 155 C200 155 200 75 230 75 C260 75 260 155 290 155 C320 155 320 75 350 75 C380 75 380 155 410 155 C440 155 440 115 470 115 H530" fill="none" stroke="url(#wave)" stroke-width="22" stroke-linecap="round"/>
    <g fill="#fff" stroke="#3fb5a6" stroke-width="2">
      <circle cx="110" cy="75" r="20"/><circle cx="170" cy="155" r="20"/><circle cx="230" cy="75" r="20"/><circle cx="290" cy="155" r="20"/><circle cx="350" cy="75" r="20"/><circle cx="410" cy="155" r="20"/>
    </g>
    <circle cx="15" cy="115" r="5" fill="#1e88e5"/><circle cx="530" cy="115" r="5" fill="#1e88e5"/>
    <g font-family="Maven Pro, sans-serif" font-size="7" fill="#1e88e5" text-anchor="middle"><text x="15" y="135">Start</text><text x="530" y="135">Finish</text></g>
    <g font-family="Maven Pro, sans-serif" font-size="6" fill="#999" text-anchor="middle">
      <text x="110" y="30">Input short text here</text><text x="230" y="30">Input short text here</text><text x="350" y="30">Input short text here</text>
      <text x="170" y="205">Input short text here</text><text x="290" y="205">Input short text here</text><text x="410" y="205">Input short text here</text>
    </g>
  </svg>
  <div class="foot-logo"><i></i>Copperleaf Studio</div>
  <div class="page-no"><svg width="46" height="46"><use href="#pageno"/></svg><span>17</span></div>
</section>

<!-- 18 Donut charts -->
<section class="slide numbered">
  <h2 class="title abs" style="left:20px;top:12px;font-size:18px;color:#16324f">Chart Title Here</h2>
  <svg class="abs" style="left:20px;top:75px" width="540" height="180" viewBox="0 0 540 180" font-family="Maven Pro, sans-serif">
    <g transform="translate(70,60)">
      <circle r="36" fill="#e7f6f2"/><circle r="36" fill="none" stroke="#eee" stroke-width="7"/>
      <circle r="36" fill="none" stroke="#3fb5a6" stroke-width="7" stroke-dasharray="169.6 226.2" transform="rotate(-90)"/>
      <text y="5" text-anchor="middle" font-size="14" fill="#3fb5a6">75 %</text>
    </g>
    <g transform="translate(200,60)">
      <circle r="36" fill="#eef6e4"/><circle r="36" fill="none" stroke="#eee" stroke-width="7"/>
      <circle r="36" fill="none" stroke="#7fbf6a" stroke-width="7" stroke-dasharray="192.3 226.2" transform="rotate(-90)"/>
      <text y="5" text-anchor="middle" font-size="14" fill="#7fbf6a">85 %</text>
    </g>
    <g transform="translate(330,60)">
      <circle r="36" fill="#fdf3e3"/><circle r="36" fill="none" stroke="#eee" stroke-width="7"/>
      <circle r="36" fill="none" stroke="#f2a93b" stroke-width="7" stroke-dasharray="214.9 226.2" transform="rotate(-90)"/>
      <text y="5" text-anchor="middle" font-size="14" fill="#f2a93b">95 %</text>
    </g>
    <g transform="translate(460,60)">
      <circle r="36" fill="#fdecec"/><circle r="36" fill="none" stroke="#eee" stroke-width="7"/>
      <circle r="36" fill="none" stroke="#e8737a" stroke-width="7" stroke-dasharray="169.6 226.2" transform="rotate(-90)"/>
      <text y="5" text-anchor="middle" font-size="14" fill="#e8737a">75 %</text>
    </g>
    <g text-anchor="middle" font-size="9" font-weight="700" fill="#16324f">
      <text x="70" y="125">Chart Title</text><text x="200" y="125">Chart Title</text><text x="330" y="125">Chart Title</text><text x="460" y="125">Chart Title</text>
    </g>
    <g text-anchor="middle" font-size="6" fill="#888">
      <text x="70" y="138">Creativity is the key to</text><text x="70" y="146">success in the great</text>
      <text x="200" y="138">Creativity is the key to</text><text x="200" y="146">success in the great</text>
      <text x="330" y="138">Creativity is the key to</text><text x="330" y="146">success in the great</text>
      <text x="460" y="138">Creativity is the key to</text><text x="460" y="146">success in the great</text>
    </g>
  </svg>
  <div class="foot-logo"><i></i>Copperleaf Studio</div>
  <div class="page-no"><svg width="46" height="46"><use href="#pageno"/></svg><span>18</span></div>
</section>

</main>
</body>
</html>
```